Business Card Design For Office Furniture Clearance Company

Kestrel Office Clearance - our company name pretty much explains what we do, we clear offices for high end clients, mainly plc's and large international companies.

We require a nice looking business card that displays professionalism but without being too serious.

It would be nice to see just a little more than a conventional boring business card, make sure you add some flare.

Industry/Entity Type

Office Furniture

Contact Information for Business Card

CARD 1

Tom Pardew
Director
tom@kestrelofficeclearance.co.uk
m: 07700 513928

t: 01632 419063
www.kestrelofficeclearance.co.uk

Kestrel Office Clearance
Unit K4 B
3-7 Ferndale Lane
Ashcombe
Wexford Vale
ZZ9 4QX

free office clearances… you cant get better than that.

CARD 2

Henry Walbrook
Director
henry@kestrelofficeclearance.co.uk
m: 07700 628157

t: 01632 419063

Kestrel Office Clearance
Unit K4 B
3-7 Ferndale Lane
Ashcombe
Wexford Vale
ZZ9 4QX

Font styles to use
Sans Serif

Requirements
Must have
• A white background - as we have a blue logo.
Nice to have
• Nice use of the logo - play around with this and dissect it.

```html
<!DOCTYPE html>
<html lang="en">
<head>
<meta charset="utf-8">
<title>Kestrel Office Clearance – Business Card</title>
<link rel="stylesheet" href="https://fonts.googleapis.com/css2?family=Open+Sans:wght@400;600;700&display=swap">
<style>
  :root {
    --page-bg: #e6e8eb;
    --card-white: #ffffff;
    --brand-blue: #1a6fb3;
    --brand-blue-light: #3d92d3;
    --brand-blue-pale: #7fb6de;
    --ink: #2b2b2b;
    --ink-soft: #6b6b6b;
  }
  * { margin: 0; padding: 0; box-sizing: border-box; }
  html, body {
    width: 1200px; height: 997px; overflow: hidden;
    background: var(--page-bg);
    font-family: "Open Sans", Arial, sans-serif;
  }
  .card {
    position: absolute; left: 250px;
    width: 700px; height: 400px;
    background: var(--card-white);
    border-radius: 22px; overflow: hidden;
    box-shadow: 0 10px 30px rgba(0,0,0,0.18);
  }
  .card--front { top: 68px; }
  .card--back { top: 528px; }
  .card__art { position: absolute; inset: 0; width: 100%; height: 100%; }

  /* front */
  .holder { position: absolute; left: 44px; top: 150px; }
  .holder__name { color: var(--brand-blue-light); font-size: 30px; font-weight: 600; line-height: 1.1; }
  .holder__role { color: var(--ink-soft); font-size: 16px; }
  .company-name {
    position: absolute; right: 150px; top: 40px;
    color: var(--brand-blue); font-size: 18px; font-weight: 700;
  }
  .contact-list { position: absolute; left: 30px; top: 282px; list-style: none; }
  .contact-list li {
    display: flex; align-items: center; gap: 10px;
    color: #fff; font-size: 15px; line-height: 22px;
  }
  .contact-list svg { width: 15px; height: 15px; flex: none; }
  .contact-list .indent { padding-left: 25px; }

  /* back */
  .services-title {
    position: absolute; right: 34px; top: 20px;
    color: #fff; font-size: 22px; font-weight: 600;
  }
  .service-caption {
    position: absolute; width: 160px; text-align: center;
    color: var(--ink); font-size: 13px; line-height: 1.3; top: 212px;
  }
  .service-caption--survey { left: 90px; }
  .service-caption--clear { left: 270px; top: 194px; }
  .service-caption--disposal { left: 450px; top: 224px; }
  .big-mark {
    position: absolute; left: 30px; top: 320px;
    color: #fff; font-size: 34px; font-weight: 700;
  }
  .website {
    position: absolute; right: 34px; bottom: 26px;
    color: var(--brand-blue); font-size: 18px; font-weight: 600;
  }
</style>
</head>
<body>

<section class="card card--front">
  <svg class="card__art" viewBox="0 0 700 400" aria-hidden="true">
    <path d="M0 250 C210 245 390 190 560 105 L700 40 L700 400 L0 400Z" fill="var(--brand-blue-light)"/>
    <path d="M0 272 C220 265 400 215 575 130 L700 72 L700 400 L0 400Z" fill="var(--brand-blue)"/>
    <circle cx="600" cy="90" r="46" fill="var(--brand-blue)" stroke="#fff" stroke-width="6"/>
  </svg>
  <div class="company-name">Kestrel Office Clearance</div>
  <div class="holder">
    <div class="holder__name">Tom Pardew</div>
    <div class="holder__role">Director</div>
  </div>
  <ul class="contact-list">
    <li><svg viewBox="0 0 16 16"><rect width="16" height="16" rx="3" fill="#fff"/><rect x="5" y="2.5" width="6" height="11" rx="1" fill="var(--brand-blue)"/></svg>07700 513928</li>
    <li><svg viewBox="0 0 16 16"><rect width="16" height="16" rx="3" fill="#fff"/><path d="M4 5c1 4 3 6 7 7l1.5-1.5-2-1.5-1 1c-1.5-.7-2.8-2-3.5-3.5l1-1L5.5 3.5Z" fill="var(--brand-blue)"/></svg>01632 419063</li>
    <li><svg viewBox="0 0 16 16"><rect width="16" height="16" rx="3" fill="#fff"/><rect x="3" y="4.5" width="10" height="7" fill="none" stroke="var(--brand-blue)" stroke-width="1.4"/><path d="M3 4.5 8 9l5-4.5" fill="none" stroke="var(--brand-blue)" stroke-width="1.4"/></svg>tom@kestrelofficeclearance.co.uk</li>
    <li><svg viewBox="0 0 16 16"><rect width="16" height="16" rx="3" fill="#fff"/><path d="M8 2.5a3.5 3.5 0 0 0-3.5 3.5C4.5 9 8 13.5 8 13.5S11.5 9 11.5 6A3.5 3.5 0 0 0 8 2.5Z" fill="var(--brand-blue)"/><circle cx="8" cy="6" r="1.3" fill="#fff"/></svg>Unit K4 B, 3-7 Ferndale Lane, Ashcombe, Wexford Vale</li>
    <li class="indent">ZZ9 4QX</li>
  </ul>
</section>

<section class="card card--back">
  <svg class="card__art" viewBox="0 0 700 400" aria-hidden="true">
    <path d="M0 0H700V225C560 130 140 130 0 225Z" fill="var(--brand-blue-light)"/>
    <path d="M0 0H700V200C560 105 140 105 0 200Z" fill="var(--brand-blue)"/>
    <circle cx="80" cy="380" r="155" fill="var(--brand-blue-pale)" opacity="0.85"/>
    <g stroke="#fff" stroke-width="6" fill="var(--brand-blue)">
      <circle cx="170" cy="158" r="40"/>
      <circle cx="350" cy="140" r="40"/>
      <circle cx="530" cy="170" r="40"/>
    </g>
    <path d="M156 142c3 14 11 23 25 28l5-5-7-6-4 4c-5-3-9-7-11-12l4-4-6-8Z" fill="#fff"/>
    <path d="M180 140a10 10 0 0 1 8 8M180 132a18 18 0 0 1 16 16" fill="none" stroke="#fff" stroke-width="2.5" stroke-linecap="round"/>
    <g fill="none" stroke="#fff" stroke-width="5" stroke-linecap="round">
      <path d="M514 162a17 17 0 0 1 22-12"/>
      <path d="M548 168a17 17 0 0 1-8 21"/>
      <path d="M530 190a17 17 0 0 1-17-14"/>
    </g>
    <g fill="#fff">
      <path d="M532 142l10 8-12 4Z"/>
      <path d="M546 194l-13-1 8-10Z"/>
      <path d="M505 172l6-12 5 11Z"/>
    </g>
  </svg>
  <div class="services-title">Our Services</div>
  <p class="service-caption service-caption--survey">Call or email to arrange your survey</p>
  <p class="service-caption service-caption--clear">We clear your office for FREE</p>
  <p class="service-caption service-caption--disposal">Ethical disposal of all office furniture</p>
  <div class="big-mark">Kestrel</div>
  <div class="website">www.kestrelofficeclearance.co.uk</div>
</section>

</body>
</html>
```